Stationary for Tovin Consulting

Hi

I am after stationary designs for my company - Tovin Consulting. I have a logo - recently designed by ArtHarbor. Tovin ( nivot spelt backwards ) is a sales consultancy - including sales training, sales coaching and business management.

I have attached some of the artwork I already have, as well as a few ideas
1. Use supplied logo's
2. back of business card to use the logo with the dark background and white text
3. details to be included on card are
Logo
Delia Marquand
p: +61409827316
e: delia@tovinconsulting.com.au
w: www.tovinconsulting.com.au
PO Box 412, Kelby Heights, Victoria, 3187

4. I am after designs for business cards, A4 letterhead and A5 letterhead

Thanks in Advance

Delia

Industry/Entity Type

It Company

```html
<!DOCTYPE html>
<html lang="en">
<head>
<meta charset="utf-8">
<title>Tovin Consulting Stationery</title>
<link rel="stylesheet" href="https://fonts.googleapis.com/css2?family=Open+Sans:wght@400;600;700;800&display=swap">
<style>
  :root {
    --slate: #2f4354;
    --flame: #e2472a;
    --paper: #ffffff;
    --ink: #3a3f45;
    --muted: #7a8189;
    --backdrop: #ececec;
    --font: "Open Sans", Arial, sans-serif;
  }
  * { box-sizing: border-box; margin: 0; padding: 0; }
  html, body { width: 1200px; height: 795px; overflow: hidden; }
  body { background: var(--backdrop); font-family: var(--font); color: var(--ink); position: relative; }

  .sheet { position: absolute; background: var(--paper); box-shadow: 0 2px 6px rgba(0,0,0,.18); overflow: hidden; }
  .band { position: absolute; left: 0; top: 0; width: 100%; display: block; }

  .wordmark { font-family: var(--font); font-weight: 800; color: var(--slate); letter-spacing: .02em; line-height: 1; white-space: nowrap; }
  .wordmark--light { color: var(--paper); }

  /* Letterheads */
  .letterhead--a4 { left: 30px; top: 40px; width: 380px; height: 537px; }
  .letterhead--a5 { left: 440px; top: 40px; width: 300px; height: 424px; }
  .letterhead .wordmark { position: absolute; right: 26px; }
  .letterhead--a4 .wordmark { top: 66px; font-size: 17px; }
  .letterhead--a5 .wordmark { top: 54px; font-size: 14px; }
  .letter-body { position: absolute; left: 32px; right: 32px; }
  .letterhead--a4 .letter-body { top: 118px; font-size: 7px; line-height: 1.55; }
  .letterhead--a5 .letter-body { top: 96px; left: 26px; right: 26px; font-size: 6px; line-height: 1.5; }
  .recipient { margin-bottom: 10px; }
  .recipient strong { font-weight: 700; }
  .letter-body p { margin-bottom: 8px; }
  .signature { width: 60px; height: 18px; background: #e4e6e8; margin: 6px 0 4px; }
  .letter-footer { position: absolute; right: 26px; text-align: right; font-size: 5.5px; line-height: 1.6; color: var(--muted); }
  .letterhead--a4 .letter-footer { bottom: 20px; }
  .letterhead--a5 .letter-footer { bottom: 16px; font-size: 5px; }
  .base-rule { position: absolute; left: 0; bottom: 0; width: 100%; height: 5px; background: var(--slate); }

  /* Envelopes */
  .envelope { width: 400px; height: 200px; left: 770px; }
  .envelope--back { top: 40px; }
  .envelope--front { top: 260px; }
  .flap { position: absolute; left: 0; top: 0; width: 100%; height: 58px; background: var(--slate); border-radius: 0 0 22px 22px; }
  .flap .wordmark { position: absolute; left: 50%; top: 50%; transform: translate(-50%, -50%); font-size: 16px; }
  .envelope--front .sender { position: absolute; left: 26px; bottom: 26px; display: flex; align-items: center; gap: 12px; }
  .envelope--front .wordmark { font-size: 18px; }
  .sender-rule { width: 1px; height: 30px; background: var(--slate); }
  .sender-details { font-size: 6px; line-height: 1.6; color: var(--muted); }

  /* Business cards */
  .card { width: 280px; height: 171px; top: 490px; }
  .card--front { left: 440px; }
  .card--back { left: 750px; background: var(--slate); }
  .card--back .wordmark { position: absolute; left: 50%; top: 50%; transform: translate(-50%, -50%); font-size: 22px; }
  .card-person { position: absolute; right: 18px; top: 36px; text-align: right; }
  .card-name { font-size: 13px; font-weight: 700; color: var(--flame); }
  .card-role { font-size: 7px; color: var(--muted); margin-top: 2px; }
  .card--front .wordmark { position: absolute; left: 18px; top: 80px; font-size: 14px; }
  .card-contacts { position: absolute; left: 18px; top: 104px; list-style: none; font-size: 7px; line-height: 1.7; }
  .card-contacts li { display: flex; align-items: center; gap: 5px; }
  .card-contacts svg { width: 8px; height: 8px; flex: none; }
</style>
</head>
<body>

<section class="sheet letterhead letterhead--a4" aria-label="A4 letterhead">
  <svg class="band" viewBox="0 0 100 22" preserveAspectRatio="none" height="118">
    <path d="M0 0H100V3C62 4 28 9 0 17Z" fill="var(--slate)"/>
    <path d="M0 19C26 11 58 5 100 4.2V5C60 7 30 13 0 21Z" fill="var(--flame)"/>
  </svg>
  <div class="wordmark">TOVIN CONSULTING</div>
  <div class="letter-body">
    <div class="recipient">To,<br><strong>Mr Jonah Reyes</strong><br>Operations Manager<br>Harbour Logistics</div>
    <p>Thank you for meeting with our team last week. We have prepared a sales training plan that suits your staff and your current growth targets for the coming year.</p>
    <p>The program combines coaching sessions, field visits and clear reporting so managers can track progress each month and adjust goals as results come in.</p>
    <p>We would welcome the chance to discuss the next steps with you and your leadership group at a time that works best for you.</p>
    <p>Thanks and Regards,</p>
    <div class="signature" role="img" aria-label="Handwritten signature"></div>
  </div>
  <div class="letter-footer">delia@tovinconsulting.com.au | www.tovinconsulting.com.au<br>PO Box 412, Kelby Heights, Victoria, 3187</div>
  <div class="base-rule"></div>
</section>

<section class="sheet letterhead letterhead--a5" aria-label="A5 letterhead">
  <svg class="band" viewBox="0 0 100 22" preserveAspectRatio="none" height="94">
    <path d="M0 0H100V3C62 4 28 9 0 17Z" fill="var(--slate)"/>
    <path d="M0 19C26 11 58 5 100 4.2V5C60 7 30 13 0 21Z" fill="var(--flame)"/>
  </svg>
  <div class="wordmark">TOVIN CONSULTING</div>
  <div class="letter-body">
    <div class="recipient">To,<br><strong>Mr Jonah Reyes</strong><br>Operations Manager<br>Harbour Logistics</div>
    <p>Thank you for meeting with our team last week. We have prepared a sales training plan that suits your staff and your current growth targets for the coming year.</p>
    <p>The program combines coaching sessions, field visits and clear reporting so managers can track progress each month and adjust goals as results come in.</p>
    <p>Thanks and Regards,</p>
    <div class="signature" role="img" aria-label="Handwritten signature"></div>
  </div>
  <div class="letter-footer">delia@tovinconsulting.com.au | www.tovinconsulting.com.au<br>PO Box 412, Kelby Heights, Victoria, 3187</div>
  <div class="base-rule"></div>
</section>

<section class="sheet envelope envelope--back" aria-label="Envelope back">
  <div class="flap"><div class="wordmark wordmark--light">TOVIN CONSULTING</div></div>
</section>

<section class="sheet envelope envelope--front" aria-label="Envelope front">
  <svg class="band" viewBox="0 0 100 30" preserveAspectRatio="none" height="90">
    <path d="M70 0H100V0C86 3 76 12 66 30H58C68 14 78 4 92 0Z" fill="var(--slate)"/>
    <path d="M100 3V5C84 9 72 18 62 30H57C68 16 82 7 100 3Z" fill="var(--flame)"/>
  </svg>
  <div class="sender">
    <div class="wordmark">TOVIN CONSULTING</div>
    <div class="sender-rule"></div>
    <div class="sender-details">delia@tovinconsulting.com.au<br>www.tovinconsulting.com.au<br>PO Box 412, Kelby Heights, Victoria, 3187</div>
  </div>
</section>

<section class="sheet card card--front" aria-label="Business card front">
  <svg class="band" viewBox="0 0 100 40" preserveAspectRatio="none" height="68">
    <path d="M0 0H100V2C60 5 28 18 0 38Z" fill="var(--slate)" opacity="0"/>
    <path d="M0 0H36C22 10 10 22 0 36Z" fill="var(--slate)"/>
    <path d="M0 38C14 22 40 10 100 6V7.5C44 12 18 24 0 40Z" fill="var(--flame)"/>
  </svg>
  <div class="card-person">
    <div class="card-name">Delia Marquand</div>
    <div class="card-role">Sales Consultant</div>
  </div>
  <div class="wordmark">TOVIN CONSULTING</div>
  <ul class="card-contacts">
    <li><svg viewBox="0 0 8 8"><circle cx="4" cy="4" r="4" fill="var(--slate)"/><path d="M2.6 2.2l.8-.2.4 1-.5.4a3 3 0 0 0 1.3 1.3l.4-.5 1 .4-.2.8c-1.9.1-3.3-1.3-3.2-3.2z" fill="#fff"/></svg>p: +61409827316</li>
    <li><svg viewBox="0 0 8 8"><circle cx="4" cy="4" r="4" fill="var(--slate)"/><rect x="2" y="2.8" width="4" height="2.6" fill="none" stroke="#fff" stroke-width=".6"/><path d="M2 2.8l2 1.5 2-1.5" fill="none" stroke="#fff" stroke-width=".6"/></svg>e: delia@tovinconsulting.com.au</li>
    <li><svg viewBox="0 0 8 8"><circle cx="4" cy="4" r="4" fill="var(--slate)"/><circle cx="4" cy="4" r="2" fill="none" stroke="#fff" stroke-width=".6"/><path d="M2 4h4M4 2v4" stroke="#fff" stroke-width=".5"/></svg>w: www.tovinconsulting.com.au</li>
    <li><svg viewBox="0 0 8 8"><circle cx="4" cy="4" r="4" fill="var(--slate)"/><path d="M4 6.3C3 5 2.6 4.3 2.6 3.5a1.4 1.4 0 0 1 2.8 0c0 .8-.4 1.5-1.4 2.8z" fill="#fff"/></svg>PO Box 412, Kelby Heights, Victoria, 3187</li>
  </ul>
</section>

<section class="sheet card card--back" aria-label="Business card back">
  <div class="wordmark wordmark--light">TOVIN CONSULTING</div>
</section>

</body>
</html>
```